Business card and insta posting square

This is for 2 separate projects...

1...a double sided business card for online business (no address) to hand to businesses to get them to list their details on my online directory. the butterfly logo is to be used on the business card.

2.... a posting square for Instagram to write inspirational quotes over the top of to post....with a small butterfly logo somewhere on it (in a corner maybe)....the square is to have a thin, solid green outline around the edge of it, and a faded picture through the background that will allow me to write text over the top of it that will be easily readable.
I would like the same box for all Instagram quote posts for consistency ..

Target Market(s)

spiritual , yoga, meditation, wellness......

Industry/Entity Type

Wellness

Contact Information for Business Card

Details for Business Card...
Tending A Bright Garden
Your Complete Wellness Directory
www.tendingabrightgarden.example
insta/FB/pinterest/twitter
*List Your Business for FREE *

Colors
33b8a4
34a7d8
3276b5
876aae
9bcb3c

Requirements
Must have
• butterfly logo included on business card
• insta post square can use the butterfly logo OR the TABG green square uploaded in the images
Nice to have
• greens

```html
<!DOCTYPE html>
<html lang="en">
<head>
<meta charset="utf-8">
<title>Tending A Bright Garden – Business Card</title>
<link rel="stylesheet" href="https://fonts.googleapis.com/css2?family=Anton&family=Open+Sans:wght@400;600&family=Parisienne&display=swap">
<style>
  :root {
    --page-bg: #e4e4e6;
    --card-white: #f3f3f3;
    --violet-deep: #5c0a82;
    --violet-text: #4f1f9a;
    --indigo-edge: #3a4ea3;
    --blue-band: #3276b5;
    --green-script: #52a32a;
    --teal: #33b8a4;
    --sky: #34a7d8;
    --lilac: #876aae;
    --lime: #9bcb3c;
    --url-grey: #3a3a3a;
  }
  * { box-sizing: border-box; margin: 0; padding: 0; }
  html, body {
    width: 1200px;
    height: 1015px;
    overflow: hidden;
  }
  body {
    background: var(--page-bg);
    font-family: "Open Sans", Arial, sans-serif;
    display: flex;
    flex-direction: column;
    align-items: center;
    justify-content: center;
    gap: 40px;
  }
  .card {
    position: relative;
    width: 780px;
    height: 446px;
    overflow: hidden;
    box-shadow: 0 6px 18px rgba(0, 0, 0, 0.18);
  }

  /* Front */
  .card-front {
    background: radial-gradient(ellipse 70% 90% at 50% 50%, var(--violet-deep) 0%, #551289 45%, var(--indigo-edge) 100%);
    display: flex;
    flex-direction: column;
    align-items: center;
    justify-content: center;
    gap: 22px;
  }
  .brand-dot {
    width: 70px;
    height: 70px;
    border-radius: 50%;
    background: #ffffff;
  }
  .brand-name {
    color: #ffffff;
    font-weight: 600;
    font-size: 38px;
    letter-spacing: 0.5px;
  }

  /* Back */
  .card-back {
    background: var(--card-white);
  }
  .back-brand {
    position: absolute;
    top: 70px;
    right: 70px;
    display: flex;
    align-items: center;
    gap: 16px;
  }
  .back-brand .brand-dot {
    width: 56px;
    height: 56px;
    background: var(--lilac);
  }
  .back-brand .brand-name {
    color: var(--violet-text);
    font-size: 30px;
  }
  .social-row {
    position: absolute;
    top: 222px;
    right: 56px;
    display: flex;
    gap: 5px;
  }
  .social-dot {
    width: 22px;
    height: 22px;
    border-radius: 50%;
  }
  .social-dot.one { background: var(--blue-band); }
  .social-dot.two { background: #c8283a; }
  .social-dot.three { background: var(--sky); }
  .social-dot.four { background: var(--indigo-edge); }

  .headline {
    position: absolute;
    left: 52px;
    top: 236px;
    font-family: "Anton", Impact, sans-serif;
    color: var(--violet-text);
    font-size: 44px;
    line-height: 1.0;
    text-transform: uppercase;
    letter-spacing: 0.5px;
  }
  .headline .line-two { padding-left: 22px; }
  .site-url {
    position: absolute;
    left: 62px;
    top: 338px;
    font-size: 19px;
    font-weight: 600;
    color: var(--url-grey);
  }
  .tagline {
    position: absolute;
    left: 118px;
    top: 366px;
    font-family: "Parisienne", cursive;
    font-size: 38px;
    color: var(--green-script);
  }
  .edge-band {
    position: absolute;
    left: 0;
    bottom: 0;
    width: 100%;
    height: 60px;
  }
</style>
</head>
<body>

  <section class="card card-front" aria-label="Card front">
    <div class="brand-dot"></div>
    <p class="brand-name">Tending A Bright Garden</p>
  </section>

  <section class="card card-back" aria-label="Card back">
    <div class="back-brand">
      <div class="brand-dot"></div>
      <p class="brand-name">Tending A Bright Garden</p>
    </div>

    <div class="social-row" aria-label="Social channels">
      <span class="social-dot one"></span>
      <span class="social-dot two"></span>
      <span class="social-dot three"></span>
      <span class="social-dot four"></span>
    </div>

    <h1 class="headline">
      <span>Your Complete</span><br>
      <span class="line-two">Wellness Directory</span>
    </h1>
    <p class="site-url">www.tendingabrightgarden.example</p>
    <p class="tagline">List Your Business for FREE</p>

    <svg class="edge-band" viewBox="0 0 780 60" preserveAspectRatio="none" aria-hidden="true">
      <defs>
        <linearGradient id="bandViolet" x1="0" y1="0" x2="1" y2="0">
          <stop offset="0" stop-color="#5c0a82"/>
          <stop offset="1" stop-color="#4b2fa0"/>
        </linearGradient>
      </defs>
      <polygon points="330,52 780,10 780,52" fill="url(#bandViolet)"/>
      <rect x="0" y="52" width="780" height="8" fill="#3276b5"/>
    </svg>
  </section>

</body>
</html>
```